We need an attractive business card design that is modern and inviting. We like the blue and yellow (or gold) colors that are displayed with the logo. The business should communicate trust, experience, and integrity.

Target Market(s)

Residential and Commercial

Industry/Entity Type

Business

Contact Information for Business Card

Recessed Lighting
LED Retro Fit
Sign Repair
Alarms and Cameras
Mobile Home Services
24hr service calls

Font styles to use
Serif
Sans Serif

Colors
3176b5
0455a3
fece3e
fbee3e

Requirements
Must have
• Brondle Electric
• Owner: Marcus Tivane
• Licensed and Insured
• TECL #58917
Nice to have
• Exquisite Detail!!
• Over 20 years of experience
Should not have
• Nothing boring or traditional!!!

```html
<!DOCTYPE html>
<html lang="en">
<head>
<meta charset="utf-8">
<title>Brondle Electric – Business Card</title>
<link href="https://fonts.googleapis.com/css2?family=Source+Sans+3:wght@400;600;700&display=swap" rel="stylesheet">
<style>
  :root {
    --stage: #ecebe8;
    --card: #1f2a34;
    --ink: #ffffff;
    --ink-soft: #e3e6ea;
    --blue: #1c7fd8;
    --yellow: #fbee3e;
    --gold: #fece3e;
  }
  * { margin: 0; padding: 0; box-sizing: border-box; }
  html, body { width: 1200px; height: 900px; overflow: hidden; }
  body {
    background: var(--stage);
    font-family: "Source Sans 3", sans-serif;
    position: relative;
  }
  .card {
    position: absolute;
    background: var(--card);
    box-shadow: 0 6px 18px rgba(0,0,0,.18);
  }
  .card--front { left: 238px; top: 62px; width: 555px; height: 342px; }
  .card--back  { left: 459px; top: 518px; width: 559px; height: 342px; }

  /* front */
  .brand-mark {
    position: absolute; left: 97px; top: 78px;
    width: 170px; height: 170px;
    border: 7px solid var(--blue); border-radius: 50%;
    display: flex; align-items: center; justify-content: center;
    text-align: center;
  }
  .brand-mark__name {
    color: var(--yellow); font-weight: 700; font-size: 22px; line-height: 1.1;
  }
  .contact { position: absolute; left: 302px; top: 78px; color: var(--ink-soft); }
  .contact__name { color: var(--ink); font-weight: 700; font-size: 20px; line-height: 26px; }
  .contact__role { font-size: 15px; line-height: 18px; }
  .contact__cred { margin-top: 11px; font-size: 15px; line-height: 20px; }
  .contact__lines { margin-top: 19px; font-size: 15px; line-height: 20px; }
  .contact__line { display: flex; align-items: center; gap: 9px; }
  .contact__line svg { width: 12px; height: 12px; fill: var(--ink); flex: none; }
  .tagline {
    position: absolute; left: 0; right: 0; top: 280px;
    text-align: center; color: var(--yellow); font-size: 24px;
  }

  /* back */
  .back-mark {
    position: absolute; left: 243px; top: 77px;
    width: 74px; height: 74px;
    border: 5px solid var(--blue); border-radius: 50%;
  }
  .back-name {
    position: absolute; left: 0; right: 0; top: 148px;
    text-align: center; color: var(--yellow);
    font-weight: 700; font-size: 30px; letter-spacing: 1px; text-transform: uppercase;
  }
  .services {
    position: absolute; left: 0; right: 0; top: 229px;
    text-align: center; color: var(--yellow); font-size: 16px; line-height: 23px;
  }
  .services__hours { font-weight: 700; }
</style>
</head>
<body>
  <section class="card card--front">
    <div class="brand-mark"><span class="brand-mark__name">Brondle<br>Electric</span></div>
    <div class="contact">
      <p class="contact__name">Marcus Tivane</p>
      <p class="contact__role">Owner</p>
      <p class="contact__cred">Licensed &amp; Insured<br>TECL #58917</p>
      <div class="contact__lines">
        <p class="contact__line">
          <svg viewBox="0 0 24 24" aria-hidden="true"><path d="M6.6 10.8a15.1 15.1 0 0 0 6.6 6.6l2.2-2.2a1 1 0 0 1 1-.25 11.4 11.4 0 0 0 3.6.57 1 1 0 0 1 1 1V20a1 1 0 0 1-1 1A17 17 0 0 1 3 4a1 1 0 0 1 1-1h3.5a1 1 0 0 1 1 1c0 1.25.2 2.45.57 3.57a1 1 0 0 1-.25 1z"/></svg>
          55501487
        </p>
        <p class="contact__line">
          <svg viewBox="0 0 24 24" aria-hidden="true"><path d="M2 5h20v14H2z M2 5l10 8 10-8" /></svg>
          info@brondle.com
        </p>
      </div>
    </div>
    <p class="tagline">Over 20 Years of experience</p>
  </section>

  <section class="card card--back">
    <div class="back-mark"></div>
    <p class="back-name">Brondle Electric</p>
    <div class="services">
      <p>Residential and Commercial | Recessed Lighting | LED Retro Fit</p>
      <p>Sign Repair | Alarms and Cameras | Mobile Home Services</p>
      <p class="services__hours">24hr service calls</p>
    </div>
  </section>
</body>
</html>
```